Upmarket Dessert Lounge needs a Business Card Design

We are an upmarket dessert lounge needing a business card to match our image.

We want something that is simple yet beautiful, feminine, classy, sophisticated and elegant. We want it to stand out and don't mind if it is bold.

The design should include our logo and colours of red or maroon with gold highlights. We don't mind if black is used.

Marlow & Quince

Target Market(s)

For those who like to indulge or treat themselves and give in to their temptations on good quality desserts.

Industry/Entity Type

Business

Requirements
Must have
• Must include our logo and our name

Marlow & Quince

M & Q

```html
<!DOCTYPE html>
<html lang="en">
<head>
<meta charset="utf-8">
<title>Marlow &amp; Quince — Business Card</title>
<link rel="stylesheet" href="https://fonts.googleapis.com/css2?family=Open+Sans:wght@400;700&display=swap">
<style>
  :root {
    --maroon: #7a1416;
    --gold: #f6c98c;
    --cream: #fbe7c8;
    --peach-light: #fff3e3;
    --peach: #fcd29d;
    --ink: #333333;
    --paper: #ffffff;
    --backdrop: #e4e4e4;
  }
  * { margin: 0; padding: 0; box-sizing: border-box; }
  html, body {
    width: 956px; height: 1200px; overflow: hidden;
    background: var(--backdrop);
    font-family: "Open Sans", Arial, sans-serif;
    color: var(--ink);
  }
  .card {
    position: absolute; left: 75px; width: 797px; height: 455px;
    border-radius: 30px; overflow: hidden;
  }
  .card-front { top: 88px; background: var(--paper); }
  .card-back {
    top: 634px;
    background: radial-gradient(ellipse at center, var(--peach-light) 0%, #fde4c0 55%, var(--peach) 100%);
  }
  .swoosh { position: absolute; left: 0; top: 0; }
  .side-band { position: absolute; right: 0; top: 0; width: 60px; height: 100%; background: var(--maroon); }
  .gold-stripe { position: absolute; left: 729px; width: 8px; background: var(--gold); }
  .gold-stripe.upper { top: 0; height: 150px; }
  .gold-stripe.lower { top: 304px; height: 151px; }
  .brand-name {
    position: absolute; left: 25px; top: 110px; width: 390px;
    text-align: center; font-size: 37px; font-weight: 400;
    color: var(--maroon); letter-spacing: 1px;
  }
  .person { position: absolute; right: 82px; top: 72px; text-align: right; font-size: 22px; line-height: 31px; }
  .person .name { font-weight: 700; }
  .contact { position: absolute; right: 77px; text-align: right; font-size: 19px; line-height: 36px; }
  .contact.phones { top: 186px; }
  .contact.online { top: 350px; line-height: 33px; }
  .icon { position: absolute; left: 742px; width: 20px; height: 20px; fill: var(--paper); }
  .address { position: absolute; left: 69px; top: 366px; font-size: 19px; line-height: 27px; }
  .home-icon { position: absolute; left: 36px; top: 383px; width: 22px; height: 22px; fill: var(--ink); }
  .monogram {
    position: absolute; left: 0; top: 0; width: 100%; height: 100%;
    display: flex; align-items: center; justify-content: center;
    font-size: 110px; font-weight: 400; color: var(--maroon);
  }
</style>
</head>
<body>
  <section class="card card-front" aria-label="Business card front">
    <svg class="swoosh" width="797" height="455" viewBox="0 0 797 455" aria-hidden="true">
      <path d="M470 455 C620 330 700 200 720 0" fill="none" stroke="var(--cream)" stroke-width="16"/>
      <path d="M575 455 C665 330 712 200 728 0" fill="none" stroke="var(--cream)" stroke-width="10"/>
    </svg>
    <div class="side-band"></div>
    <div class="gold-stripe upper"></div>
    <div class="gold-stripe lower"></div>

    <div class="brand-name">MARLOW &amp; QUINCE</div>

    <div class="person">
      <div class="name">Your Name</div>
      <div class="title">Designation</div>
    </div>

    <div class="contact phones">
      <div>123-456-7890</div>
      <div>123-456-7890</div>
      <div>123-456-7890</div>
    </div>
    <svg class="icon" style="top:194px" viewBox="0 0 20 20" aria-label="Phone"><path d="M2 8c0-4 16-4 16 0v2h-4V8H6v2H2z"/><rect x="4" y="11" width="12" height="6" rx="1"/></svg>
    <svg class="icon" style="top:229px" viewBox="0 0 20 20" aria-label="Mobile"><rect x="6" y="3" width="9" height="15" rx="1.5"/><rect x="8" y="5" width="5" height="4" fill="var(--maroon)"/><rect x="7" y="0" width="1.5" height="4"/></svg>
    <svg class="icon" style="top:264px" viewBox="0 0 20 20" aria-label="Fax"><rect x="6" y="3" width="8" height="5"/><rect x="3" y="8" width="14" height="7" rx="1"/><rect x="5" y="11" width="10" height="2" fill="var(--maroon)"/></svg>

    <div class="contact online">
      <div>name@yourwebsite.com</div>
      <div>www.marlowandquince.com</div>
    </div>
    <svg class="icon" style="top:358px" viewBox="0 0 20 20" aria-label="Email"><text x="10" y="16" text-anchor="middle" font-size="17" font-weight="700" fill="var(--paper)" font-family="Open Sans, sans-serif">@</text></svg>
    <svg class="icon" style="top:393px" viewBox="0 0 20 20" aria-label="Website"><circle cx="10" cy="10" r="7.5"/><path d="M4 8h12M4 12h12M10 2.5c-3 4-3 11 0 15M10 2.5c3 4 3 11 0 15" stroke="var(--maroon)" stroke-width="1" fill="none"/></svg>

    <svg class="home-icon" viewBox="0 0 22 22" aria-label="Address"><path d="M11 2 1 11h3v9h5v-6h4v6h5v-9h3z"/></svg>
    <div class="address">
      <div>0000, Street Name</div>
      <div>City Name, Country Code.</div>
    </div>
  </section>

  <section class="card card-back" aria-label="Business card back">
    <div class="monogram">M &amp; Q</div>
  </section>
</body>
</html>
```